Brisk Rig Vitals: Truck Smoke Check Company

I need a logo for a truck health company in California called "Brisk Rig Vitals". This company does smoke checks for heavy duty diesel trucks under the Pacific Clean Skies Council (PCSC) called HD I/M tests. I want the brand to feel reliable.

Target Market(s)

California Diesel Trucks. Individual truck drivers and trucking companies.

Industry/Entity Type

Automotive

Contact Information for Business Card

Company Name, Slogan, contact information. marcotellez@briskrigvitals-example.com

```html
<!DOCTYPE html>
<html lang="en">
<head>
<meta charset="utf-8">
<title>Brisk Rig Vitals – Business Card</title>
<link rel="stylesheet" href="https://fonts.googleapis.com/css2?family=Montserrat:wght@400;500;600;700&display=swap">
<style>
  :root {
    --backdrop: #adadad;
    --card-black: #030303;
    --card-light: #dcdcdc;
    --ink-white: #ffffff;
    --ink-dark: #111111;
    --ink-muted: #6f6f6f;
    --smoke: rgba(190, 190, 190, 0.28);
  }
  * { box-sizing: border-box; margin: 0; padding: 0; }
  html, body {
    width: 1200px; height: 1200px; overflow: hidden;
    background: var(--backdrop);
    font-family: "Montserrat", sans-serif;
  }
  .stage {
    width: 1200px; height: 1200px;
    display: flex; flex-direction: column; align-items: center; justify-content: center;
    gap: 48px;
  }
  .card {
    width: 900px; height: 514px; position: relative; overflow: hidden;
    box-shadow: 0 10px 24px rgba(0,0,0,0.28);
  }
  .smoke {
    position: absolute;
    background: radial-gradient(ellipse at center, var(--smoke) 0%, rgba(160,160,160,0.12) 45%, rgba(0,0,0,0) 72%);
  }
  /* Front */
  .card-front { background: var(--card-black); }
  .card-front .smoke { left: 470px; top: 20px; width: 300px; height: 440px; }
  .front-brand {
    position: absolute; left: 0; right: 0; top: 210px; text-align: center;
  }
  .front-brand .company {
    color: var(--ink-white); font-weight: 600; font-size: 44px; letter-spacing: 1.5px;
    text-transform: uppercase;
  }
  .front-brand .slogan {
    color: var(--ink-muted); font-weight: 400; font-size: 30px; margin-top: 6px; letter-spacing: 0.5px;
  }
  /* Back */
  .card-back { display: flex; }
  .back-identity {
    width: 360px; flex: none; background: var(--card-black); position: relative;
  }
  .back-identity .smoke { left: 60px; top: 300px; width: 320px; height: 230px; }
  .person { position: absolute; left: 64px; top: 215px; }
  .person .name {
    color: var(--ink-white); font-weight: 600; font-size: 30px; letter-spacing: 1.5px;
    text-transform: uppercase; white-space: nowrap;
  }
  .person .role {
    color: var(--ink-muted); font-size: 20px; letter-spacing: 3px; text-transform: uppercase; margin-top: 4px;
  }
  .back-details {
    flex: 1; background: var(--card-light); position: relative; padding: 58px 36px 0 48px;
  }
  .back-details .company {
    color: var(--ink-dark); font-weight: 700; font-size: 24px; letter-spacing: 1px; text-transform: uppercase;
    text-align: center; margin-left: -48px; margin-right: -36px;
  }
  .contact-list { list-style: none; margin-top: 120px; }
  .contact-list li {
    display: flex; align-items: flex-start; gap: 12px;
    color: var(--ink-dark); font-weight: 500; font-size: 17px; line-height: 1.3; margin-bottom: 16px;
  }
  .contact-list span { min-width: 0; overflow-wrap: anywhere; padding-top: 2px; }
  .contact-list svg { flex: none; width: 26px; height: 26px; }
</style>
</head>
<body>
<main class="stage">
  <section class="card card-front">
    <div class="smoke" role="img" aria-label="Soft drifting smoke"></div>
    <div class="front-brand">
      <p class="company">Brisk Rig Vitals</p>
      <p class="slogan">Your Slogan Here</p>
    </div>
  </section>

  <section class="card card-back">
    <div class="back-identity">
      <div class="smoke" role="img" aria-label="Soft drifting smoke"></div>
      <div class="person">
        <p class="name">Dana Morrow</p>
        <p class="role">Director</p>
      </div>
    </div>
    <div class="back-details">
      <p class="company">Brisk Rig Vitals</p>
      <ul class="contact-list">
        <li>
          <svg viewBox="0 0 28 28" aria-hidden="true"><circle cx="14" cy="14" r="14" fill="#111"/><path d="M9 8c1-1 2-1 2.6 0l1.3 2c.4.7.2 1.3-.3 1.8l-.8.7c.8 1.8 2.1 3.1 3.8 3.9l.7-.8c.5-.5 1.1-.7 1.8-.3l2 1.3c1 .6 1 1.6 0 2.6-1.4 1.4-3.6 1.2-6.4-1-2.4-2-4-4.3-4.6-6.4-.3-1.3 0-2.2-.1-2.8z" fill="#fff"/></svg>
          <span>5550142389</span>
        </li>
        <li>
          <svg viewBox="0 0 28 28" aria-hidden="true"><circle cx="14" cy="14" r="14" fill="#111"/><rect x="8" y="9.5" width="12" height="9" rx="1" fill="none" stroke="#fff" stroke-width="1.5"/><path d="M8.5 10.5 14 15l5.5-4.5" fill="none" stroke="#fff" stroke-width="1.5"/></svg>
          <span>marcotellez@briskrigvitals-example.com</span>
        </li>
        <li>
          <svg viewBox="0 0 28 28" aria-hidden="true"><circle cx="14" cy="14" r="14" fill="#111"/><circle cx="14" cy="14" r="6.5" fill="none" stroke="#fff" stroke-width="1.5"/><ellipse cx="14" cy="14" rx="3" ry="6.5" fill="none" stroke="#fff" stroke-width="1.3"/><path d="M7.5 14h13" stroke="#fff" stroke-width="1.3"/></svg>
          <span>www.briskrigvitals-example.com</span>
        </li>
        <li>
          <svg viewBox="0 0 28 28" aria-hidden="true"><circle cx="14" cy="14" r="14" fill="#111"/><path d="M14 6.5a5 5 0 0 0-5 5c0 3.8 5 9.5 5 9.5s5-5.7 5-9.5a5 5 0 0 0-5-5z" fill="#fff"/><circle cx="14" cy="11.5" r="2" fill="#111"/></svg>
          <span>123 Anywhere St.,<br>Any City, ST 12345</span>
        </li>
      </ul>
    </div>
  </section>
</main>
</body>
</html>
```